Veltrano - Mechanic/Collision Center Business Card

We're looking for a business card design for our mechanic/ collision repair shop.

Can be with colours or monochromatic.

See the attached files.

Many thanks

```html
<!DOCTYPE html>
<html lang="en">
<head>
<meta charset="utf-8">
<title>Veltrano – Business Card</title>
<link rel="stylesheet" href="https://fonts.googleapis.com/css2?family=Open+Sans:wght@400;600;700;800&display=swap">
<style>
  :root {
    --backdrop: #c2c2c2;
    --card-dark: #1a1d20;
    --brand-blue: #1e9fd8;
    --band-steel: #346b87;
    --plate-dark: #15181b;
    --paper: #fafafa;
    --paper-shade: #ececec;
    --ink: #1b1b1b;
    --ink-muted: #858585;
    --white: #ffffff;
  }
  * { margin: 0; padding: 0; box-sizing: border-box; }
  html, body {
    width: 1200px; height: 1200px; overflow: hidden;
    background: var(--backdrop);
    font-family: "Open Sans", Arial, sans-serif;
  }
  .canvas { position: relative; width: 1200px; height: 1200px; }

  /* Front card */
  .card { position: absolute; left: 246px; width: 715px; height: 447px; border-radius: 19px; overflow: hidden; }
  .card-front { top: 86px; background: var(--card-dark); }
  .front-tab { position: absolute; left: 342px; top: 0; width: 31px; height: 60px; background: var(--brand-blue); }
  .front-brand {
    position: absolute; left: 0; right: 0; top: 190px;
    display: flex; justify-content: center; align-items: center; gap: 14px;
    color: var(--white); font-weight: 800; font-size: 50px; letter-spacing: 1px;
  }
  .brand-square { width: 22px; height: 22px; background: var(--brand-blue); }
  .front-band { position: absolute; left: 0; right: 0; bottom: 0; height: 36px; background: var(--brand-blue); }
  .front-band-center { position: absolute; left: 205px; width: 306px; bottom: 0; height: 36px; background: var(--band-steel); }
  .postal-plate {
    position: absolute; left: 205px; width: 306px; top: 361px; height: 50px;
    background: var(--plate-dark);
    display: flex; align-items: center; justify-content: center;
    color: var(--white); font-size: 20px;
  }

  /* Back card */
  .card-back { top: 682px; background: var(--paper); }
  .back-texture { position: absolute; left: 0; top: 0; width: 351px; height: 100%; background: var(--paper-shade); }
  .back-brand {
    position: absolute; left: 0; width: 351px; top: 218px; text-align: center;
    color: var(--ink); font-weight: 800; font-size: 42px; letter-spacing: 1px;
  }
  .divider-tick { position: absolute; left: 340px; width: 11px; background: var(--brand-blue); }
  .divider-tick.top { top: 0; height: 66px; }
  .divider-tick.bottom { bottom: 0; height: 67px; }
  .edge-strip { position: absolute; right: 0; top: 0; width: 38px; height: 100%; background: var(--plate-dark); }
  .edge-accent { position: absolute; right: 0; top: 66px; width: 38px; height: 314px; background: var(--brand-blue); }
  .edge-line { position: absolute; right: 38px; top: 66px; width: 9px; height: 314px; background: var(--plate-dark); }

  .identity { position: absolute; left: 369px; top: 85px; }
  .company { font-weight: 700; font-size: 25px; letter-spacing: 1.5px; color: var(--ink); line-height: 1.1; }
  .role { font-size: 19px; letter-spacing: 1px; color: var(--ink-muted); line-height: 1.2; }

  .contacts { position: absolute; left: 367px; top: 203px; list-style: none; }
  .contacts li { display: flex; align-items: center; gap: 12px; height: 24px; margin-bottom: 19px; font-size: 18.5px; color: var(--ink); }
  .contacts li:nth-child(3) { margin-bottom: 22px; }
  .contacts svg { width: 24px; height: 24px; flex: none; }
</style>
</head>
<body>
<div class="canvas">

  <section class="card card-front" aria-label="Card front">
    <div class="front-tab"></div>
    <div class="front-brand"><span class="brand-square"></span>VELTRANO</div>
    <div class="front-band"></div>
    <div class="front-band-center"></div>
    <div class="postal-plate">Postal code : 1900-318 Lisboa</div>
  </section>

  <section class="card card-back" aria-label="Card back">
    <div class="back-texture" role="img" aria-label="Light grey diagonal line texture"></div>
    <div class="back-brand">VELTRANO</div>
    <div class="divider-tick top"></div>
    <div class="divider-tick bottom"></div>
    <div class="edge-strip"></div>
    <div class="edge-line"></div>
    <div class="edge-accent"></div>

    <div class="identity">
      <p class="company">VELTRANO, LDA</p>
      <p class="role">FOUNDER / CEO</p>
    </div>

    <ul class="contacts">
      <li>
        <svg viewBox="0 0 24 24"><circle cx="12" cy="12" r="12" fill="#1b1b1b"/><path d="M8.6 6.5l1.6-.4 1.2 2.8-1.1 1a7 7 0 0 0 3.8 3.8l1-1.1 2.8 1.2-.4 1.6c-.2.6-.8 1-1.5.9A10 10 0 0 1 7.7 8c0-.7.3-1.3.9-1.5z" fill="#fff"/></svg>
        +351 210 555 014
      </li>
      <li>
        <svg viewBox="0 0 24 24"><circle cx="12" cy="12" r="12" fill="#1b1b1b"/><circle cx="12" cy="12" r="6" fill="none" stroke="#fff" stroke-width="1.6"/><path d="M6 12h12M12 6c-2 2-2 10 0 12M12 6c2 2 2 10 0 12" fill="none" stroke="#fff" stroke-width="1.2"/></svg>
        hello@veltrano-auto.pt
      </li>
      <li>
        <svg viewBox="0 0 24 24"><circle cx="12" cy="12" r="12" fill="#1e9fd8"/><path d="M12 5.5a4 4 0 0 0-4 4c0 3 4 8 4 8s4-5 4-8a4 4 0 0 0-4-4z" fill="#fff"/><circle cx="12" cy="9.5" r="1.5" fill="#1e9fd8"/></svg>
        veltrano-auto.pt/oficina
      </li>
      <li>
        <svg viewBox="0 0 24 24"><circle cx="12" cy="12" r="12" fill="#1e9fd8"/><path d="M12 5.5a4 4 0 0 0-4 4c0 3 4 8 4 8s4-5 4-8a4 4 0 0 0-4-4z" fill="#fff"/><circle cx="12" cy="9.5" r="1.5" fill="#1e9fd8"/></svg>
        Rua das Oficinas, 14
      </li>
    </ul>
  </section>

</div>
</body>
</html>
```